Velmora Trade Hall (front page)

We need a design of a front page for our Velmora Trade Hall website (vth.co.uk). Our company is based in the United Kingdom and offers investors from all over the world an opportunity to invest into bitcoin and litecoin.

We have been developing this cutting edge technology for past 2 years based on our in depth knowledge on conventional stock and currency trading technology and methodology. We have run many test against penetration, security and stability and now are ready to deploy.

Recent news about vulnerability of such platforms leave a great deal of unease from retail investors about investing into cryptocurrency. We are set to challenge this attitude. Our background is payments in particular regulated environment in the UK. We are keen to apply our wealth of experience to provide secure and reliable trading platform and advance cryptocurrency as means of legal tender.

The front page should be based on the feel and look of our current technology vth.co.uk. Some of you have already been involved in logo design for our company, please see the attached mockups. The page should have this minimalist design, very clean and light.

Seek inspiration form www.korvelin.net, www.trusmarq.com, vip.plomwerth.com and other bitcoin exchanges.

We look forward to receiving your ideas.

You can also refer to our social pages:
https://www.facebook.com/vth.co.uk
https://twitter.com/vth_uk

We would like you to focus your efforts at designing the page in such a way so that it is very easy for visitor be open an account with the exchange. We must focus at informing the visitor about the bitcoin, how to my buy, how to sell, look at the general overview of the maker and CONVERTING him/her sing up. This is the most important!!

Regards,
Oren

Reason: Dear all, We are very keen on getting this design done right the first time. The key success is conversion of visitors to subscribers and then to traders. It is absolutely essential make the registration process as streamlined as possible! When we are calling them to act by "Change the world one bitcoin at a time" we should give them a opportunity to provide us with relevant account creation details: email, password, confirm password. Please visit quenzo.co.uk for ideas. Secondly, tell them what is a bitcoin, why a bitcoin is a good investment and how to invest. Finally, it is important to inform visitors of "who we are", what sets us apart from other exchanges, tell them about our experience. In our view graphs and live order books are important but they might turn some visitors away especially the ones that are not accustomed to online trading. Think of what would you like to see on the page if you wanted YOURSELF to invest. What would make you to create an account and use it? Think what will work, we are here to revolutionise how people do business.... any wild ideas put them to us. OUR BUDGET JUST GONE UP!!!

Target Market(s)

A combination of professional and consumer bitcoin investors.

Requirements
Must have
• News section

```html
<!DOCTYPE html>
<html lang="en">
<head>
<meta charset="utf-8">
<title>Velmora Trade Hall</title>
<link href="https://fonts.googleapis.com/css2?family=Open+Sans:wght@400;600;700&family=Great+Vibes&display=swap" rel="stylesheet">
<style>
:root{
  --ink:#222;
  --muted:#555;
  --brand:#1ea6dd;
  --brand-dark:#0f8cc2;
  --brand-light:#7fcbea;
  --ticker-bg:#0b0b0b;
  --ticker-text:#3fc3f2;
  --footer:#2b2b2b;
  --sell-row:#fadcdc;
  --buy-row:#dcedf8;
  --line:#d7d7d7;
  --friendwall:#3b5a9a;
  --rss:#f07a1c;
  --circlenet:#5b5b5b;
}
*{box-sizing:border-box;margin:0;padding:0}
html,body{width:1200px;height:2469px;overflow:hidden}
body{position:relative;background:#fff;font-family:"Open Sans",Arial,sans-serif;color:var(--ink)}
.abs{position:absolute}

/* ticker */
.ticker{left:0;top:0;width:1200px;height:44px;background:var(--ticker-bg);font-size:15px;line-height:44px}
.ticker span{position:absolute;color:var(--ticker-text)}
.ticker .ticker-label{color:#fff;font-weight:700}

/* header */
.brand{left:44px;top:62px;display:flex;align-items:center;gap:12px}
.brand-dot{width:26px;height:26px;border-radius:50%;background:var(--brand)}
.brand-name{font-size:20px;font-weight:600;color:#333;letter-spacing:1px;text-transform:uppercase}
.tagline{left:333px;top:58px;width:860px;font-family:"Great Vibes",cursive;font-size:72px;line-height:76px;color:var(--brand);white-space:nowrap}

/* nav */
.nav-tab{top:153px;height:40px;background:var(--brand);color:#fff;font-size:15px;font-weight:600;text-align:center;line-height:40px;border-radius:6px 6px 0 0;box-shadow:inset 0 -4px 0 rgba(255,255,255,.25)}

/* hero */
.hero{left:0;top:190px;width:1200px;height:410px;background:linear-gradient(180deg,#36bdeb 0%,#22a8df 100%);overflow:hidden}
.hero-rate{color:#fff;font-size:19px;letter-spacing:3px}
.hero-strip{left:0;top:321px;width:1200px;height:62px;background:rgba(255,255,255,.18)}
.stat-main{left:86px;top:321px;color:#fff;font-size:36px;font-weight:700;line-height:62px}
.stat-box{top:331px;height:44px;color:#fff;font-size:30px;font-weight:700;text-align:center;line-height:44px}
.stat-box.dim{left:289px;width:192px;background:rgba(255,255,255,.25)}
.stat-box.bright{left:486px;width:141px;background:rgba(255,255,255,.5)}
.hero-shadow{left:0;top:600px;width:1200px;height:40px;background:linear-gradient(#e5e5e5,#fff)}

/* features */
.feature{top:688px;width:222px}
.feature-icon{width:90px;height:90px;margin-left:32px;border-radius:50%;background:var(--brand);display:flex;align-items:center;justify-content:center}
.feature h3{margin-top:36px;font-size:25px;font-weight:400;color:#333;white-space:nowrap}
.feature p{margin-top:12px;font-size:14px;line-height:19px;color:#222}

/* account panel */
.account{left:798px;top:696px;width:350px;height:371px;background:var(--brand-light)}
.account-tabs{display:flex;height:45px;font-size:16px;font-weight:700;color:#fff}
.account-tabs .active{width:175px;background:var(--brand);text-align:center;line-height:45px}
.account-tabs .plain{flex:1;text-align:center;line-height:45px}
.field{position:absolute;left:36px;width:290px;height:45px;background:#fff;border-radius:4px;padding-left:16px;line-height:45px;color:var(--brand);font-size:17px}
.help{position:absolute;right:10px;top:12px;width:22px;height:22px;border-radius:50%;background:var(--brand);color:#fff;font-size:14px;font-weight:700;text-align:center;line-height:22px}
.remember{position:absolute;left:36px;top:196px;font-size:16px;color:#fff;display:flex;align-items:center;gap:12px}
.remember i{width:12px;height:12px;background:#fff;display:block}
.btn{position:absolute;left:36px;width:300px;height:52px;background:var(--brand);color:#fff;font-weight:700;font-size:18px;text-align:center;line-height:52px;border-radius:3px}

/* search */
.search{left:810px;top:1099px;width:331px;height:39px;background:var(--brand);color:#fff;font-size:12px;line-height:39px;padding-left:32px}

/* tweets */
.tweets{left:810px;top:1165px;width:338px;height:390px;border:1px solid #d4d4d4;background:#fff;box-shadow:0 2px 5px rgba(0,0,0,.1)}
.tweets-head{height:50px;padding:18px 16px 0;font-size:15px;font-weight:700;position:relative;border-bottom:1px solid #e0e0e0}
.tweets-badge{position:absolute;right:14px;top:8px;width:50px;height:34px;border-radius:6px;background:#9bd4f0}
.tweet{padding:14px 16px 10px;border-bottom:1px solid #e0e0e0;position:relative}
.tweet-avatar{position:absolute;left:16px;top:16px;width:32px;height:32px;border-radius:50%;background:var(--brand)}
.tweet-user{margin-left:46px;font-size:14px;font-weight:700;line-height:17px}
.tweet-user small{display:block;font-weight:400;color:#777;font-size:13px}
.tweet-date{position:absolute;right:20px;top:14px;font-size:14px;font-weight:700}
.tweet-text{margin-top:14px;font-size:14px;font-weight:700;line-height:18px}
.tweet-more{font-size:12px;color:#777;font-weight:700;margin-top:4px}

/* follow */
.side-title{left:805px;font-size:26px;color:#555;width:345px;padding-bottom:10px;border-bottom:2px dashed #ccc}
.social{left:815px;width:228px;height:47px;border-radius:24px;color:#fff;font-size:16px;font-weight:600;display:flex;align-items:center;gap:12px;padding-left:6px}
.social i{width:36px;height:36px;border-radius:50%;background:#fff;display:block;opacity:.9}
.social.friendwall{background:var(--friendwall)}
.social.rss{background:var(--rss)}
.social.circlenet{background:var(--circlenet)}
.count{left:1062px;width:74px;height:47px;border:1px solid #ccc;border-radius:6px;background:#f6f6f6;text-align:center;line-height:45px;font-size:17px;font-weight:600;color:#444}
.news-text{left:805px;top:2049px;width:345px;font-size:17px;line-height:21px;color:#222}

/* chart */
.chart-card{left:54px;top:1057px;width:706px;height:333px;background:#fff;box-shadow:0 2px 8px rgba(0,0,0,.25)}
.chart-title{position:absolute;left:0;top:10px;width:100%;text-align:center;font-size:12px;font-weight:700}
.chart-periods{position:absolute;left:12px;top:10px;display:flex;gap:2px}
.chart-periods span{border:1px solid #bbb;font-size:10px;padding:0 3px}
.chart-periods .on{background:#ffe97a}
.chart-tabs{position:absolute;left:0;bottom:0;width:100%;height:26px;display:flex;border-top:1px solid #ccc}
.chart-tabs span{flex:1;text-align:center;font-size:11px;line-height:26px;color:#888;border-right:1px solid #ddd;background:#f3f3f3}
.chart-tabs .on{background:#fff;color:#333}

/* orders */
.orders{left:54px;top:1412px;width:716px;height:938px;background:#fff;box-shadow:0 2px 8px rgba(0,0,0,.25)}
.orders-tabs{display:flex;height:36px;margin:8px 8px 0;border-bottom:1px solid #ccc}
.orders-tabs span{flex:1;text-align:center;font-size:14px;line-height:36px;color:#888;background:#f2f2f2;border:1px solid #ddd;border-bottom:none}
.orders-tabs .on{background:#fff;color:#333}
.orders table{position:absolute;left:8px;top:60px;width:700px;border-collapse:collapse;font-size:12.5px;color:#333}
.orders th{height:38px;font-weight:400;text-align:center;border-bottom:1px solid var(--line)}
.orders td{height:37.4px;text-align:center;border-bottom:1px solid #fff}
.orders th:first-child,.orders td:first-child{text-align:left;padding-left:16px}
.orders tr.sell td{background:var(--sell-row)}
.orders tr.buy td{background:var(--buy-row)}

/* footer */
.footer{left:0;top:2353px;width:1200px;height:116px;background:var(--footer);color:#fff;text-align:center}
.footer-links{margin-top:24px;font-size:25px;word-spacing:6px}
.footer-links b{font-weight:400;margin:0 24px}
.footer-copy{margin-top:14px;font-size:25px}
</style>
</head>
<body>

<div class="abs ticker">
  <span class="ticker-label" style="left:44px">LAST PRICE</span>
  <span style="left:143px">Last price499.12 USD</span>
  <span style="left:353px">Low price490.125 USD</span>
  <span style="left:563px">High price511.824 USD</span>
  <span style="left:773px">Volume374.6 BTC</span>
</div>

<div class="abs brand"><i class="brand-dot"></i><span class="brand-name">Velmora Trade Hall</span></div>
<div class="abs tagline">Change the world one bitcoin at a time</div>

<div class="abs nav-tab" style="left:99px;width:173px">Home</div>
<div class="abs nav-tab" style="left:237px;width:170px">API trades</div>
<div class="abs nav-tab" style="left:412px;width:186px">Terms and Conditions</div>
<div class="abs nav-tab" style="left:612px;width:144px">Buy and Sell</div>
<div class="abs nav-tab" style="left:800px;width:143px">Support</div>
<div class="abs nav-tab" style="left:983px;width:148px">Contacts</div>

<section class="abs hero">
  <div class="abs hero-rate" style="left:432px;top:72px">Sell BTC 604.29200 USD</div>
  <div class="abs hero-rate" style="left:235px;top:203px">Buy BTC 605.49800 USD</div>
  <div class="abs hero-strip"></div>
  <div class="abs stat-main">230 000</div>
  <div class="abs stat-box dim">90 000</div>
  <div class="abs stat-box bright">82 000</div>
  <svg class="abs" style="left:0;top:0" width="1200" height="410" aria-hidden="true">
    <g fill="none" stroke="#fff" stroke-width="3" opacity=".85">
      <circle cx="790" cy="328" r="92"/>
      <circle cx="790" cy="328" r="62"/>
      <path d="M790 296 V328 H818"/>
      <circle cx="1040" cy="328" r="92"/>
      <circle cx="1235" cy="328" r="92"/>
    </g>
    <circle cx="1040" cy="328" r="62" fill="#fff" opacity=".7" role="img" aria-label="Globe icon"/>
  </svg>
</section>
<div class="abs hero-shadow"></div>

<div class="abs feature" style="left:74px">
  <div class="feature-icon">
    <svg width="46" height="46" viewBox="0 0 46 46" fill="#fff" aria-hidden="true">
      <ellipse cx="23" cy="10" rx="15" ry="6"/><rect x="8" y="14" width="30" height="7" rx="3"/><rect x="8" y="23" width="30" height="7" rx="3"/><rect x="8" y="32" width="30" height="7" rx="3"/>
    </svg>
  </div>
  <h3>High Liquidity</h3>
  <p>Lorem ipsum dolor sit amet, consectetur adipisicing elit, sed do eiusmod tempor incididunt ut labore et dolore magna aliqua. Ut enim ad minim</p>
</div>
<div class="abs feature" style="left:332px">
  <div class="feature-icon">
    <svg width="44" height="50" viewBox="0 0 44 50" aria-hidden="true">
      <path d="M22 2 L40 9 V24 C40 36 32 44 22 48 C12 44 4 36 4 24 V9 Z" fill="none" stroke="#fff" stroke-width="4"/>
    </svg>
  </div>
  <h3>High Security</h3>
  <p>Lorem ipsum dolor sit amet, consectetur adipisicing elit, sed do eiusmod tempor incididunt ut labore et dolore magna aliqua. Ut enim ad minim</p>
</div>
<div class="abs feature" style="left:590px">
  <div class="feature-icon"><span role="img" aria-label="Head with gear icon" style="width:42px;height:42px;border-radius:50%;background:#fff;display:block"></span></div>
  <h3>High Availability</h3>
  <p>Lorem ipsum dolor sit amet, consectetur adipisicing elit, sed do eiusmod tempor incididunt ut labore et dolore magna aliqua. Ut enim ad minim</p>
</div>

<aside class="abs account">
  <div class="account-tabs"><span class="active">OPEN UP ACCOUNT</span><span class="plain">LOGIN</span></div>
  <div class="field" style="top:74px">Username</div>
  <div class="field" style="top:136px">Password<span class="help">?</span></div>
  <div class="remember"><i></i>Remember me</div>
  <div class="btn" style="top:232px">SIGN IN</div>
  <div class="btn" style="top:304px">FORGOT PASSWORD?</div>
</aside>

<div class="abs search">SEARCH.......VTH
  <svg class="abs" style="right:30px;top:11px" width="18" height="18" viewBox="0 0 18 18" aria-hidden="true"><circle cx="7" cy="7" r="5.5" fill="none" stroke="#fff" stroke-width="2.5"/><path d="M11 11 L16 16" stroke="#fff" stroke-width="3"/></svg>
</div>

<div class="abs tweets">
  <div class="tweets-head">TWEETS<span class="tweets-badge"></span></div>
  <div class="tweet">
    <i class="tweet-avatar"></i>
    <div class="tweet-user">VTH<small>@vth_uk</small></div>
    <span class="tweet-date">21 Mar</span>
    <p class="tweet-text">Velmora Trade Hall is a powerful and secure cryptocurrency trading platform designed for retail and institutional investors.</p>
    <p class="tweet-more">Expand</p>
  </div>
  <div class="tweet" style="border:none">
    <i class="tweet-avatar"></i>
    <div class="tweet-user">VTH<small>@vth_uk</small></div>
    <span class="tweet-date">21 Mar</span>
    <p class="tweet-text">Change the world one bitcoin at a time.</p>
  </div>
</div>

<h2 class="abs side-title" style="top:1600px;font-weight:400">Follow Us</h2>
<div class="abs social friendwall" style="top:1691px"><i></i>Follow on Friendwall</div>
<div class="abs count" style="top:1691px">125</div>
<div class="abs social rss" style="top:1778px"><i></i>Subscribe via RSS</div>
<div class="abs count" style="top:1778px">125</div>
<div class="abs social circlenet" style="top:1869px"><i></i>Follow on Circlenet</div>
<div class="abs count" style="top:1869px">125</div>

<h2 class="abs side-title" style="top:1982px;font-weight:400">Bitcoin news</h2>
<p class="abs news-text">Lorem ipsum dolor sit amet, consectetur adipisicing elit, sed do eiusmod tempor incididunt ut labore et dolore magna aliqua. Ut enim ad minim veniam, quis nostrud exercitation ullamco laboris nisi ut aliquip ex ea commodo consequat. Duis aute irure dolor in reprehenderit in voluptate velit esse cillum dolore eu fugiat nulla pariatur. Excepteur sint occaecat</p>

<div class="abs chart-card">
  <div class="chart-periods"><span class="on">M1</span><span>M5</span><span>M15</span><span>M30</span><span>H1</span><span>H4</span></div>
  <div class="chart-title">BTC/USD</div>
  <svg class="abs" style="left:0;top:30px" width="706" height="277" aria-label="BTC/USD price line chart">
    <defs><linearGradient id="area" x1="0" y1="0" x2="0" y2="1"><stop offset="0" stop-color="#9fd4f2"/><stop offset="1" stop-color="#e6f4fc"/></linearGradient></defs>
    <g stroke="#eee" stroke-width="1"><line x1="50" y1="55" x2="706" y2="55"/><line x1="50" y1="122" x2="706" y2="122"/><line x1="50" y1="186" x2="706" y2="186"/></g>
    <g font-size="10" fill="#666" font-family="Open Sans,sans-serif">
      <text x="4" y="52">501.700</text><text x="4" y="118">500.400</text><text x="4" y="183">499.1</text>
      <text x="112" y="246">20:40</text><text x="220" y="246">20:50</text><text x="334" y="246">21:00</text><text x="445" y="246">21:10</text><text x="557" y="246">21:20</text>
    </g>
    <path d="M48 208 L120 208 L130 188 L220 186 L300 186 L330 150 L362 74 L390 150 L450 150 L478 88 L500 90 L520 150 L600 150 L628 118 L660 118 L706 136 L706 232 L48 232 Z" fill="url(#area)"/>
    <polyline points="48,208 120,208 130,188 220,186 300,186 330,150 362,74 390,150 450,150 478,88 500,90 520,150 600,150 628,118 660,118 706,136" fill="none" stroke="#5fb5e6" stroke-width="2"/>
  </svg>
  <div class="chart-tabs"><span class="on">QUOTES</span><span>CANDLES</span><span>DEPTH</span><span>VOLUME</span></div>
</div>

<div class="abs orders">
  <div class="orders-tabs"><span>Active orders</span><span class="on">All orders</span><span>Trade history</span></div>
  <table>
    <thead><tr><th>Market</th><th>Time</th><th>Type</th><th>Volume (BTC)</th><th>Price</th><th>Total (USD)</th></tr></thead>
    <tbody>
      <tr class="sell"><td>BTC/USD</td><td>Sunday, March 30, 2014 1:04:59 AM</td><td>Sell</td><td>0.00585</td><td>500.757</td><td>2.9294</td></tr>
      <tr class="sell"><td>BTC/USD</td><td>Sunday, March 30, 2014 1:04:36 AM</td><td>Sell</td><td>0.00442</td><td>502.24</td><td>2.2199</td></tr>
      <tr class="buy"><td>BTC/USD</td><td>Sunday, March 30, 2014 1:03:17 AM</td><td>Buy</td><td>2.54465</td><td>502.24</td><td>1278.0250</td></tr>
      <tr class="buy"><td>BTC/USD</td><td>Sunday, March 30, 2014 1:03:14 AM</td><td>Buy</td><td>1.76251</td><td>502.24</td><td>885.2030</td></tr>
      <tr class="buy"><td>BTC/USD</td><td>Sunday, March 30, 2014 12:52:54 AM</td><td>Buy</td><td>0.31828</td><td>502</td><td>159.7766</td></tr>
      <tr class="buy"><td>BTC/USD</td><td>Sunday, March 30, 2014 12:52:34 AM</td><td>Buy</td><td>0.26407</td><td>501.998</td><td>132.5628</td></tr>
      <tr class="buy"><td>BTC/USD</td><td>Sunday, March 30, 2014 12:52:15 AM</td><td>Buy</td><td>0.5135</td><td>501.957</td><td>257.7549</td></tr>
      <tr class="buy"><td>BTC/USD</td><td>Sunday, March 30, 2014 12:52:13 AM</td><td>Buy</td><td>0.00916</td><td>501.9</td><td>4.5974</td></tr>
      <tr class="buy"><td>BTC/USD</td><td>Sunday, March 30, 2014 12:52:13 AM</td><td>Buy</td><td>0.00441</td><td>501.299</td><td>2.2107</td></tr>
      <tr class="buy"><td>BTC/USD</td><td>Sunday, March 30, 2014 12:51:28 AM</td><td>Buy</td><td>0.02763</td><td>501.001</td><td>13.8427</td></tr>
      <tr class="sell"><td>BTC/USD</td><td>Sunday, March 30, 2014 12:49:39 AM</td><td>Sell</td><td>0.03252</td><td>501.001</td><td>16.2926</td></tr>
      <tr class="buy"><td>BTC/USD</td><td>Sunday, March 30, 2014 12:46:34 AM</td><td>Buy</td><td>0.01053</td><td>501.001</td><td>5.2755</td></tr>
      <tr class="buy"><td>BTC/USD</td><td>Sunday, March 30, 2014 12:45:00 AM</td><td>Buy</td><td>0.01722</td><td>500.96</td><td>8.6265</td></tr>
      <tr class="buy"><td>BTC/USD</td><td>Sunday, March 30, 2014 12:40:32 AM</td><td>Buy</td><td>0.51036</td><td>499.4</td><td>254.8738</td></tr>
      <tr class="sell"><td>BTC/USD</td><td>Sunday, March 30, 2014 12:40:05 AM</td><td>Sell</td><td>0.00848</td><td>499.4</td><td>4.2349</td></tr>
      <tr class="sell"><td>BTC/USD</td><td>Sunday, March 30, 2014 12:28:10 AM</td><td>Sell</td><td>0.05263</td><td>499.001</td><td>26.2624</td></tr>
      <tr class="sell"><td>BTC/USD</td><td>Sunday, March 30, 2014 12:26:42 AM</td><td>Sell</td><td>0.12097</td><td>499.01</td><td>60.3652</td></tr>
      <tr class="sell"><td>BTC/USD</td><td>Sunday, March 30, 2014 12:22:21 AM</td><td>Sell</td><td>0.00639</td><td>499.21</td><td>3.1900</td></tr>
      <tr class="sell"><td>BTC/USD</td><td>Sunday, March 30, 2014 12:21:51 AM</td><td>Sell</td><td>0.08658</td><td>499.4</td><td>43.2381</td></tr>
      <tr class="sell"><td>BTC/USD</td><td>Sunday, March 30, 2014 12:21:10 AM</td><td>Sell</td><td>0.00697</td><td>499.402</td><td>3.4808</td></tr>
      <tr class="sell"><td>BTC/USD</td><td>Sunday, March 30, 2014 12:14:56 AM</td><td>Sell</td><td>1.26582</td><td>500</td><td>632.9100</td></tr>
      <tr class="sell"><td>BTC/USD</td><td>Sunday, March 30, 2014 12:10:19 AM</td><td>Sell</td><td>0.01073</td><td>500.969</td><td>5.3754</td></tr>
    </tbody>
  </table>
</div>

<footer class="abs footer">
  <nav class="footer-links">Home<b>|</b>API trade<b>|</b>Terms and Condition<b>|</b>Contact<b>|</b>Support</nav>
  <p class="footer-copy">© 2014 Velmora Trade Hall Limited. All rights reserved</p>
</footer>

</body>
</html>
```